Machining Business Order Thank You Insert

I am looking for a business style card to include with orders that I ship. The card needs to thank the recipient for their order, and encourage them to leave a review. The card should include my business name and contact information and have an area to hand write a message.

I mainly sale on Crafvine and my own website. We are a machining an manufacturing business that are in the sale of mostly metal machined and 3d printed plastic products.

The front of the card should include the following:
Logo: (attached)
Snapgrid: https://www.instagram.com/quillforge/
Friendwall: https://www.facebook.com/QuillForge
Website: https://www.quillforge-example.com/

The back of the card needs an area to write a message

Industry/Entity Type

3D Printing, Machining, Crafvine

Contact Information for Business Card

Black or white front, white back to write a personal message

Font styles to use
Sans Serif

Colors

Designer to choose colors to be used in the design.

Requirements
Must have
• Encourage a review, social media info

```html
<!DOCTYPE html>
<html lang="en">
<head>
<meta charset="utf-8">
<title>QuillForge Thank You Insert</title>
<link rel="stylesheet" href="https://fonts.googleapis.com/css2?family=Montserrat:wght@500;600&display=swap">
<style>
  :root {
    --backdrop: #cbcbcb;
    --card: #ebebeb;
    --ink: #6b6b6b;
    --rule: #2a2a2a;
    --accent: #e2582a;
    --accent-soft: #e8805d;
  }
  * { box-sizing: border-box; margin: 0; padding: 0; }
  html, body { width: 1200px; height: 907px; overflow: hidden; }
  body {
    background: var(--backdrop);
    font-family: "Montserrat", sans-serif;
    display: flex;
    align-items: center;
    justify-content: center;
    gap: 40px;
  }
  .card {
    position: relative;
    width: 540px;
    height: 309px;
    background: var(--card);
    box-shadow: 0 8px 24px rgba(0,0,0,0.12);
  }

  /* brand lockup */
  .brand {
    display: flex;
    align-items: center;
    gap: 12px;
    white-space: nowrap;
  }
  .brand-mark {
    flex: none;
    width: 16px;
    height: 16px;
    background: var(--accent);
  }
  .brand-name {
    font-weight: 600;
    font-size: 18px;
    letter-spacing: 0.3em;
    color: var(--ink);
    text-transform: uppercase;
  }

  /* message side */
  .card--message .brand {
    position: absolute;
    top: 30px;
    left: 50%;
    transform: translateX(-50%);
  }
  .thanks {
    position: absolute;
    top: 66px;
    left: 0;
    right: 0;
    text-align: center;
    font-weight: 600;
    font-size: 15px;
    color: var(--accent);
    white-space: nowrap;
  }
  .message-area {
    position: absolute;
    left: 40px;
    right: 40px;
    top: 100px;
    height: 140px;
    border: 1px solid var(--ink);
    border-radius: 12px;
  }
  .message-area .dot {
    position: absolute;
    width: 6px;
    height: 6px;
    border-radius: 50%;
    background: var(--accent);
  }
  .dot--tl { top: 9px; left: 9px; }
  .dot--tr { top: 9px; right: 9px; }
  .dot--bl { bottom: 9px; left: 9px; }
  .dot--br { bottom: 9px; right: 9px; }
  .review-prompt {
    position: absolute;
    top: 258px;
    left: 0;
    right: 0;
    text-align: center;
    font-weight: 500;
    font-size: 13px;
    color: var(--ink);
    white-space: nowrap;
  }

  /* contact side */
  .card--contact .brand {
    position: absolute;
    top: 50%;
    left: 30px;
    transform: translateY(-50%);
  }
  .card--contact .brand-name { font-size: 16px; }
  .divider {
    position: absolute;
    left: 246px;
    top: 70px;
    bottom: 70px;
    border-left: 1.5px solid var(--rule);
  }
  .contact-list {
    position: absolute;
    left: 270px;
    top: 50%;
    transform: translateY(-50%);
    list-style: none;
    display: flex;
    flex-direction: column;
    gap: 22px;
  }
  .contact-item {
    display: flex;
    align-items: center;
    gap: 12px;
    font-weight: 500;
    font-size: 13px;
    color: var(--ink);
    white-space: nowrap;
  }
  .contact-icon {
    flex: none;
    width: 26px;
    height: 26px;
    border-radius: 50%;
    background: var(--accent-soft);
  }
  .contact-icon--web {
    background: none;
  }
</style>
</head>
<body>

  <section class="card card--message" aria-label="Card back with space for a handwritten message">
    <div class="brand">
      <span class="brand-mark"></span>
      <span class="brand-name">QuillForge</span>
    </div>
    <p class="thanks">Thank you for your order!</p>
    <div class="message-area" aria-label="Space for a handwritten message">
      <span class="dot dot--tl"></span>
      <span class="dot dot--tr"></span>
      <span class="dot dot--bl"></span>
      <span class="dot dot--br"></span>
    </div>
    <p class="review-prompt">Enjoyed it? Please leave us a review on Crafvine.</p>
  </section>

  <section class="card card--contact" aria-label="Card front with contact details">
    <div class="brand">
      <span class="brand-mark"></span>
      <span class="brand-name">QuillForge</span>
    </div>
    <div class="divider"></div>
    <ul class="contact-list">
      <li class="contact-item">
        <span class="contact-icon"></span>
        <span>Snapgrid / quillforge</span>
      </li>
      <li class="contact-item">
        <span class="contact-icon"></span>
        <span>Friendwall / quillforge</span>
      </li>
      <li class="contact-item">
        <svg class="contact-icon contact-icon--web" viewBox="0 0 26 26" aria-hidden="true">
          <circle cx="13" cy="13" r="12" fill="none" stroke="var(--accent-soft)" stroke-width="2"/>
          <circle cx="13" cy="13" r="7" fill="none" stroke="var(--accent-soft)" stroke-width="1.4"/>
          <ellipse cx="13" cy="13" rx="3" ry="7" fill="none" stroke="var(--accent-soft)" stroke-width="1.2"/>
          <line x1="6" y1="13" x2="20" y2="13" stroke="var(--accent-soft)" stroke-width="1.2"/>
        </svg>
        <span>www.quillforge-example.com</span>
      </li>
    </ul>
  </section>

</body>
</html>
```